We need a business card design for a Dubai based company .

We need a business card for a Dubai based company called "Zernova Smoking Requisites Trading LLC". We mainly import Flavoured Tobacco products and Charcoal which is used for smoking in a Hookah/Shisha and distribute to the wholesalers and retailers. Logo file is attached herewith.

```html
<!DOCTYPE html>
<html lang="en">
<head>
<meta charset="utf-8">
<title>Zernova Smoking Requisites Trading LLC — Business Card</title>
<link href="https://fonts.googleapis.com/css2?family=Open+Sans:wght@400;600&display=swap" rel="stylesheet">
<style>
  :root {
    --backdrop: #3a3a3c;
    --card-dark: #262626;
    --card-light: #ffffff;
    --brand-red: #c0393b;
    --ink: #1e1e1e;
    --white: #ffffff;
  }
  * { box-sizing: border-box; margin: 0; padding: 0; }
  html, body { width: 1200px; height: 1095px; overflow: hidden; }
  body {
    background: var(--backdrop);
    position: relative;
    font-family: "Open Sans", Arial, sans-serif;
  }
  .card {
    position: absolute;
    left: 250px;
    width: 700px;
    height: 400px;
    border-radius: 18px;
    overflow: hidden;
  }
  .card--front { top: 95px; background: var(--card-dark); }
  .card--back { top: 600px; background: var(--card-light); }

  .company {
    display: flex;
    align-items: center;
    gap: 16px;
    font-family: "Open Sans", Arial, sans-serif;
    font-weight: 600;
  }
  .company__square {
    width: 20px; height: 20px;
    background: var(--brand-red);
    flex: none;
  }
  .company__name { line-height: 1.2; }
  .company__line { display: block; }
  .company__line--main { font-size: 44px; letter-spacing: 1px; }
  .company__line--sub { font-size: 14px; letter-spacing: 0.5px; }

  .card--front .company {
    position: absolute; left: 0; right: 0; top: 150px;
    justify-content: center;
    color: var(--white);
  }
  .card--back .company {
    position: absolute; left: 40px; top: 160px;
    color: var(--ink);
  }
  .card--back .company__line--main { font-size: 36px; }
  .card--back .company__line--sub { font-size: 12px; }

  .divider { position: absolute; left: 318px; width: 2px; }
  .divider--top { top: 110px; height: 38px; background: var(--ink); }
  .divider--mid { top: 160px; height: 120px; background: var(--brand-red); }
  .divider--bottom { top: 292px; height: 36px; background: var(--ink); }

  .contact { position: absolute; left: 342px; top: 95px; width: 320px; color: var(--ink); }
  .contact__name {
    font-weight: 600;
    font-size: 25px; letter-spacing: 1.5px; color: var(--brand-red);
    line-height: 1.25;
    padding-bottom: 2px; border-bottom: 1.5px solid var(--brand-red);
  }
  .contact__role { font-size: 15px; font-weight: 600; margin-top: 4px; }
  .contact__address {
    font-size: 16px; line-height: 1.35; margin-top: 2px;
    padding-bottom: 6px; border-bottom: 1.5px solid var(--brand-red);
  }
  .contact__list { list-style: none; margin-top: 6px; }
  .contact__item { display: flex; align-items: center; gap: 8px; font-size: 16px; line-height: 1.5; }
  .contact__icon { width: 15px; height: 15px; flex: none; }

  .swoosh { position: absolute; left: 0; top: 0; width: 700px; height: 400px; }
</style>
</head>
<body>
  <section class="card card--front" aria-label="Card front">
    <div class="company">
      <span class="company__square"></span>
      <span class="company__name">
        <span class="company__line company__line--main">ZERNOVA</span>
        <span class="company__line company__line--sub">SMOKING REQUISITES TRADING LLC</span>
      </span>
    </div>
  </section>

  <section class="card card--back" aria-label="Card back">
    <svg class="swoosh" viewBox="0 0 700 400" aria-hidden="true">
      <path d="M420 400 C 510 365, 610 335, 700 310 L700 400 Z" fill="var(--brand-red)"/>
      <path d="M380 400 C 480 350, 600 318, 700 298" fill="none" stroke="var(--ink)" stroke-width="3"/>
    </svg>

    <div class="company">
      <span class="company__square"></span>
      <span class="company__name">
        <span class="company__line company__line--main">ZERNOVA</span>
        <span class="company__line company__line--sub">SMOKING REQUISITES TRADING LLC</span>
      </span>
    </div>

    <span class="divider divider--top"></span>
    <span class="divider divider--mid"></span>
    <span class="divider divider--bottom"></span>

    <div class="contact">
      <h1 class="contact__name">ROHAN MEHTA</h1>
      <p class="contact__role">Partner</p>
      <p class="contact__address">Unit 14, Al Quoz Industrial Area 3<br>Dubai, United Arab Emirates</p>
      <ul class="contact__list">
        <li class="contact__item">
          <svg class="contact__icon" viewBox="0 0 16 16" aria-hidden="true"><path d="M3 1.5l3 .5 1 3.2-1.8 1.3a9 9 0 0 0 4.3 4.3l1.3-1.8 3.2 1 .5 3c-.6.8-1.6 1.3-2.6 1.2C6 13.7 2.3 10 1.8 4.1 1.7 3.1 2.2 2.1 3 1.5z" fill="var(--brand-red)"/></svg>
          +971 4 555 0187
        </li>
        <li class="contact__item">
          <svg class="contact__icon" viewBox="0 0 16 16" aria-hidden="true"><rect x="1" y="3" width="14" height="10" fill="var(--brand-red)"/><path d="M1 3l7 6 7-6" fill="none" stroke="#fff" stroke-width="1.3"/></svg>
          info@zernovallc.com
        </li>
        <li class="contact__item">
          <svg class="contact__icon" viewBox="0 0 16 16" aria-hidden="true"><circle cx="8" cy="8" r="7" fill="var(--brand-red)"/><path d="M1 8h14M8 1v14M3 4.5h10M3 11.5h10" stroke="#fff" stroke-width="0.9" fill="none"/><ellipse cx="8" cy="8" rx="3.2" ry="7" fill="none" stroke="#fff" stroke-width="0.9"/></svg>
          www.zernovallc.com
        </li>
      </ul>
    </div>
  </section>
</body>
</html>
```